Brightpath Dentistry - Flyer - Modern & Eye catching campaign flyer

Need front & back side full page flyer designs for both 1) Grand opening 2) On-going campaign.

Attached the new dental office logo.
Attached our other dental clinic flyer designs for content.

Target Market(s)

Cosmetic dentistry

Industry/Entity Type

Health Care

Requirements
Must have
• decent, modern and eye catching marketing flyers.
Nice to have
• - Nice space
• - Highlight phone number
• - Highlight special features like convenient hours, call or text, for all ages, digital facility, etc
Should not have
• - Don't want to fill the flyer with too much wordings
• - Too many colors

```html
<!DOCTYPE html>
<html lang="en">
<head>
<meta charset="utf-8">
<title>Brightpath Dentistry – Flyer Front &amp; Back</title>
<link href="https://fonts.googleapis.com/css2?family=Bebas+Neue&family=Caveat+Brush&family=Ubuntu:wght@400;500;700&display=swap" rel="stylesheet">
<style>
  :root{
    --stage:#2d2d2d;
    --sky:#1ba8dc;
    --sky-deep:#0d8cc6;
    --white:#ffffff;
    --navy:#2b3a4f;
    --ink:#34495e;
    --logo-blue:#1e9fd6;
  }
  *{margin:0;padding:0;box-sizing:border-box}
  html,body{width:1200px;height:1200px;overflow:hidden;background:var(--stage)}
  body{position:relative;font-family:"Ubuntu",sans-serif;color:var(--white)}

  .flyer{position:absolute;width:487px;height:681px;overflow:hidden;background:var(--white)}
  .flyer--front{left:83px;top:217px}
  .flyer--back{left:634px;top:217px;width:484px;height:680px}
  .flyer__bg{position:absolute;inset:0;width:100%;height:100%}

  .abs{position:absolute}
  .photo{position:absolute;border-radius:50%;overflow:hidden}
  .photo--ring-navy{border:6px solid var(--navy)}
  .photo--ring-white{border:6px solid var(--white)}
  .photo__fill{width:100%;height:100%}

  .brand{position:absolute;left:0;right:0;top:48px;display:flex;align-items:center;justify-content:center;gap:10px}
  .brand__dot{width:26px;height:26px;border-radius:50%;background:var(--logo-blue)}
  .brand__name{font-weight:500;font-size:29px;color:var(--logo-blue);letter-spacing:.5px}

  .marker{font-family:"Caveat Brush","Bebas Neue",sans-serif;color:var(--white);line-height:1.08;font-weight:400;text-transform:uppercase}
  .specials__title{left:12px;width:244px;top:180px;text-align:center;font-size:37px}
  .rule{position:absolute;height:3px;background:var(--white)}

  .offer-list{list-style:none;left:19px;top:278px;font-size:14px;font-weight:500}
  .offer-list li{display:flex;align-items:center;gap:4px;height:24px}
  .tick-tooth{width:14px;height:14px;flex:none}

  .services__tag{left:0;top:374px;width:158px;height:30px;background:var(--navy);border-radius:0 15px 15px 0;font-size:18px;font-weight:500;padding-left:24px;line-height:30px}
  .service{position:absolute;width:104px;margin-left:-52px;text-align:center;font-size:10px;font-weight:500;line-height:1.1}
  .service svg{width:26px;height:26px;display:block;margin:0 auto 5px}
  .service small{display:block;font-size:6px;font-weight:400}

  .badge{position:absolute;border-radius:50%;background:var(--navy);border:3px solid var(--white);display:flex;flex-direction:column;align-items:center;justify-content:center;text-align:center}
  .badge--welcome{left:293px;top:271px;width:104px;height:104px}
  .badge--welcome .badge__title{font-size:17px;font-weight:500;line-height:1.1}
  .badge--welcome .badge__note{font-size:5px;line-height:1.3;margin-top:3px;border-top:1px solid var(--white);padding-top:2px}
  .badge--hours{left:296px;top:394px;width:76px;height:76px;font-family:"Bebas Neue",sans-serif;font-size:12.5px;line-height:1.1}
  .badge--insurance{left:292px;top:242px;width:104px;height:104px;font-family:"Bebas Neue",sans-serif;font-size:25px;line-height:1}

  .cta{position:absolute;left:0;right:0;background:var(--navy);display:flex;align-items:center;justify-content:center;gap:6px;font-size:23px}
  .cta strong{font-weight:700;font-size:25px}
  .cta svg{width:24px;height:24px}
  .flyer--front .cta{top:593px;height:34px}
  .flyer--back .cta{top:589px;height:37px}

  .contact{position:absolute;left:0;right:0;display:flex;align-items:center;color:var(--ink);font-size:10.5px;font-weight:700}
  .contact__item{flex:1;display:flex;align-items:center;justify-content:center;gap:6px}
  .contact__item svg{width:13px;height:13px}
  .contact__divider{width:2px;height:28px;background:var(--navy)}
  .flyer--front .contact{top:641px}
  .flyer--back .contact{top:633px}

  .question{left:18px;top:170px;font-size:31px;white-space:nowrap}
  .intro{left:18px;top:262px;width:240px;font-size:11.3px;line-height:1.2;text-align:justify}
  .signature{left:30px;top:324px;display:flex;align-items:center;gap:6px;font-size:12.5px;font-weight:700}
  .signature::before{content:"";width:48px;height:2px;background:var(--white)}
  .family__title{left:290px;top:384px;font-size:18px;font-weight:700;line-height:1.3;text-transform:uppercase}
  .feature-list{list-style:none;left:285px;top:456px;width:195px;font-size:9px;font-weight:500;line-height:1.2}
  .feature-list li{display:flex;gap:5px;margin-bottom:8px}
  .feature-list .tick-tooth{width:13px;height:13px;margin-top:1px}

  .side-label{position:absolute;top:940px;font-family:"Bebas Neue",sans-serif;font-size:42px;color:var(--white);letter-spacing:1px;transform:translateX(-50%)}
</style>
</head>
<body>

<svg width="0" height="0" style="position:absolute">
  <defs>
    <symbol id="tooth" viewBox="0 0 24 24">
      <path d="M7 3c-3 0-4 3-3.5 6 .4 2 1.2 3 1.5 5l1 6c.2 1.5 1.8 1.5 2.1 0l.9-4c.3-1.3 1.7-1.3 2 0l.9 4c.3 1.5 1.9 1.5 2.1 0l1-6c.3-2 1.1-3 1.5-5C20.5 6 19.5 3 16.5 3c-1.5 0-2.2.8-3.5.8h-2C9.7 3.8 8.5 3 7 3z" fill="none" stroke="currentColor" stroke-width="1.8" stroke-linejoin="round"/>
    </symbol>
    <symbol id="phone" viewBox="0 0 24 24">
      <circle cx="12" cy="12" r="10.5" fill="none" stroke="currentColor" stroke-width="1.8"/>
      <path d="M8.6 6.5l1.8-.3 1 2.6-1.2 1c.6 1.4 1.6 2.5 3 3.1l1-1.2 2.6 1-.3 1.8c-.2.8-1 1.3-1.8 1.1-3.4-.8-6.1-3.5-6.9-6.9-.2-.8.3-1.6 1.1-1.8z" fill="currentColor"/>
    </symbol>
    <symbol id="globe" viewBox="0 0 24 24">
      <g fill="none" stroke="currentColor" stroke-width="1.8"><circle cx="12" cy="12" r="10"/><ellipse cx="12" cy="12" rx="4.5" ry="10"/><path d="M2 12h20M4 6.5h16M4 17.5h16"/></g>
    </symbol>
    <symbol id="mail" viewBox="0 0 24 24">
      <rect x="2" y="5" width="20" height="14" fill="currentColor"/>
      <path d="M2 5l10 8 10-8" fill="none" stroke="#fff" stroke-width="1.6"/>
    </symbol>
  </defs>
</svg>

<section class="flyer flyer--front" aria-label="Flyer front">
  <svg class="flyer__bg" viewBox="0 0 487 681" preserveAspectRatio="none" aria-hidden="true">
    <defs>
      <linearGradient id="bodyFront" x1="0" y1="0" x2="1" y2="1">
        <stop offset="0" stop-color="#1fb2e4"/><stop offset="1" stop-color="#0d8cc6"/>
      </linearGradient>
    </defs>
    <rect width="487" height="681" fill="#fff"/>
    <path d="M0 75 C90 125 250 135 487 108 V593 H0 Z" fill="#2b3a4f"/>
    <path d="M0 95 C100 150 260 158 487 130 V593 H0 Z" fill="url(#bodyFront)"/>
  </svg>

  <div class="brand">
    <span class="brand__dot"></span>
    <span class="brand__name">Brightpath Dentistry</span>
  </div>

  <h1 class="abs marker specials__title">Grand Opening<br>Specials</h1>
  <div class="rule" style="left:42px;top:264px;width:175px"></div>

  <ul class="abs offer-list">
    <li><svg class="tick-tooth"><use href="#tooth"/></svg>Free Kids Dental Screening</li>
    <li><svg class="tick-tooth"><use href="#tooth"/></svg>$25 Adults Dental Screening</li>
    <li><svg class="tick-tooth"><use href="#tooth"/></svg>15% off on Treatment Plan</li>
  </ul>

  <div class="abs services__tag">Our Services</div>

  <div class="service" style="left:59px;top:422px"><svg><use href="#tooth"/></svg>Root Canal Therapy</div>
  <div class="service" style="left:168px;top:422px"><svg><use href="#tooth"/></svg>Glow Teeth Whitening</div>
  <div class="service" style="left:268px;top:422px"><svg><use href="#tooth"/></svg>Extractions</div>
  <div class="service" style="left:59px;top:480px"><svg><use href="#tooth"/></svg>Dentures</div>
  <div class="service" style="left:168px;top:480px"><svg><use href="#tooth"/></svg>Implants</div>
  <div class="service" style="left:263px;top:480px"><svg><use href="#tooth"/></svg>Veneers</div>
  <div class="service" style="left:59px;top:536px"><svg><use href="#tooth"/></svg>ClearFit Aligners<small>(Invisible braces)</small></div>
  <div class="service" style="left:168px;top:536px"><svg><use href="#tooth"/></svg>Night Guards</div>
  <div class="service" style="left:265px;top:536px"><svg><use href="#tooth"/></svg>Crown &amp;<br>Bridge</div>

  <div class="photo photo--ring-navy" style="left:285px;top:125px;width:206px;height:206px">
    <div class="photo__fill" role="img" aria-label="Photo of a smiling family of four" style="background:linear-gradient(135deg,#e9e2d6,#c9a98a 55%,#8ebfd8)"></div>
  </div>
  <div class="badge badge--welcome">
    <span class="badge__title">New<br>Patients<br>Welcome</span>
    <span class="badge__note">Opening special offers valid until<br><b>June 15, 2017</b><br>by Appointment only</span>
  </div>

  <div class="photo photo--ring-white" style="left:305px;top:385px;width:190px;height:190px">
    <div class="photo__fill" role="img" aria-label="Photo of a young patient in a dental chair viewing an X-ray on a tablet" style="background:linear-gradient(160deg,#eef2f5,#c7d3dc 45%,#2f6fb8)"></div>
  </div>
  <div class="badge badge--hours">Convenient<br>Evening &amp;<br>Saturday<br>Hours</div>

  <div class="cta">Call or Text Us Now : <svg><use href="#phone"/></svg><strong>555.204.7713</strong></div>
  <div class="contact">
    <span class="contact__item"><svg style="color:var(--logo-blue)"><use href="#globe"/></svg>www.BrightpathDental.com</span>
    <span class="contact__divider"></span>
    <span class="contact__item"><svg style="color:var(--logo-blue)"><use href="#mail"/></svg>info@BrightpathDental.com</span>
  </div>
</section>

<section class="flyer flyer--back" aria-label="Flyer back">
  <svg class="flyer__bg" viewBox="0 0 484 680" preserveAspectRatio="none" aria-hidden="true">
    <defs>
      <linearGradient id="bodyBack" x1="0" y1="0" x2="1" y2="1">
        <stop offset="0" stop-color="#1fb2e4"/><stop offset="1" stop-color="#0d8cc6"/>
      </linearGradient>
    </defs>
    <rect width="484" height="680" fill="#fff"/>
    <path d="M0 95 C120 150 260 170 484 130 V589 H0 Z" fill="url(#bodyBack)"/>
    <path d="M0 78 C110 130 250 148 484 112 V130 C260 170 120 150 0 98 Z" fill="#2b3a4f"/>
  </svg>
  <div class="abs" role="img" aria-label="Photo of gloved hands polishing teeth on a dental model" style="left:0;top:0;width:484px;height:130px;clip-path:path('M0 0H484V112C250 148 110 130 0 78Z');background:linear-gradient(120deg,#f1f1f1,#cfcfcf 50%,#e6d3c3)"></div>

  <h2 class="abs marker question">Looking for Dentist<br>Close to Home ?</h2>
  <div class="rule" style="left:18px;top:247px;width:173px"></div>

  <p class="abs intro">Come and See Us for Professional Services and Care. Our dentists and staff are experts in the field of advanced dentistry and will help you achieve your perfect smile.</p>
  <div class="abs signature">Dr. Maren Holt, D.D.S.</div>

  <div class="photo photo--ring-navy" style="left:283px;top:72px;width:206px;height:206px">
    <div class="photo__fill" role="img" aria-label="Photo of a smiling mature couple" style="background:linear-gradient(135deg,#f4f1ec,#e0c2a4 55%,#bfa792)"></div>
  </div>
  <div class="badge badge--insurance">All<br>Insurance<br>Accepted</div>

  <div class="photo photo--ring-navy" style="left:7px;top:348px;width:206px;height:206px">
    <div class="photo__fill" role="img" aria-label="Photo of a smiling family of four" style="background:linear-gradient(135deg,#f3efe9,#d9b596 55%,#a9c7d6)"></div>
  </div>
  <div class="photo photo--ring-white" style="left:162px;top:471px;width:106px;height:106px">
    <div class="photo__fill" role="img" aria-label="Close-up photo of a bright white smile with red lips" style="background:radial-gradient(circle,#ffffff 20%,#c8202b 55%,#f1d6c8)"></div>
  </div>

  <h3 class="abs family__title">Family &amp; Cosmetic<br>Dentistry</h3>
  <div class="rule" style="left:290px;top:439px;width:194px"></div>

  <ul class="abs feature-list">
    <li><svg class="tick-tooth"><use href="#tooth"/></svg><span>State-Of-The-Art equipment and paperless facility.</span></li>
    <li><svg class="tick-tooth"><use href="#tooth"/></svg><span>Filled with entertainment devices for patient comfort.</span></li>
    <li><svg class="tick-tooth"><use href="#tooth"/></svg><span>Same-day appointment for DENTAL EMERGENCIES</span></li>
    <li><svg class="tick-tooth"><use href="#tooth"/></svg><span>Helping community with routine free kids dental screening.</span></li>
  </ul>

  <div class="cta">Call or Text Us Now : <svg><use href="#phone"/></svg><strong>555.204.7713</strong></div>
  <div class="contact">
    <span class="contact__item"><svg style="color:var(--logo-blue)"><use href="#globe"/></svg>www.BrightpathDental.com</span>
    <span class="contact__divider"></span>
    <span class="contact__item"><svg style="color:var(--logo-blue)"><use href="#mail"/></svg>info@BrightpathDental.com</span>
  </div>
</section>

<div class="side-label" style="left:319px">Front</div>
<div class="side-label" style="left:845px">Back</div>

</body>
</html>
```